July 4th Postcard to existing clients

5x7 postcard wishing our clients happy 4th of July. Card should read on the back "Thank You For Being A Valued Client!. Stay Safe And Enjoy Your Independence Day Celebrations!"

Patriotic theme with fireworks is ideal. We are a law firm so should still have a feel of professionalism while still being fun since it is for a fun holiday.

```html
<!DOCTYPE html>
<html lang="en">
<head>
<meta charset="utf-8">
<title>Independence Day Client Postcard</title>
<link rel="stylesheet" href="https://fonts.googleapis.com/css2?family=Montserrat:wght@400;900&family=Oswald:wght@700&family=Yellowtail&family=Damion&display=swap">
<style>
  :root {
    --stage: #c9c9c9;
    --paper: #ffffff;
    --red: #c4161c;
    --red-deep: #8e0f14;
    --orange: #ee7a1e;
    --gold: #f6c44a;
    --teal: #4f8a86;
    --navy: #1f3264;
    --navy-deep: #142246;
    --ink: #1a1f36;
    --night: #1c1012;
    --rule: #222222;
    --brand-grey: #6a6a70;
    --white: #ffffff;
  }
  html, body {
    margin: 0;
    padding: 0;
    width: 800px;
    height: 1200px;
    overflow: hidden;
    background: var(--stage);
  }
  .canvas {
    position: relative;
    width: 800px;
    height: 1200px;
  }
  .postcard {
    position: absolute;
    left: 10px;
    width: 772px;
    height: 551px;
    overflow: hidden;
  }
  .postcard--front { top: 46px; }
  .postcard--back { top: 620px; background: var(--paper); }
  .postcard svg { display: block; }
  .headline-block { font-family: "Montserrat", sans-serif; font-weight: 900; }
  .date-block { font-family: "Oswald", sans-serif; font-weight: 700; }
  .script { font-family: "Yellowtail", cursive; }
  .thanks-script { font-family: "Damion", cursive; }
  .address-side {
    position: absolute;
    left: 428px;
    top: 0;
    width: 344px;
    height: 551px;
  }
  .stamp-box {
    position: absolute;
    left: 230px;
    top: 26px;
    width: 82px;
    height: 88px;
    border: 1px solid var(--rule);
  }
  .address-line {
    position: absolute;
    left: 18px;
    width: 296px;
    height: 0;
    border-top: 1px solid var(--rule);
  }
  .brand-name {
    position: absolute;
    left: 0;
    right: 22px;
    top: 484px;
    text-align: right;
    font-family: "Montserrat", sans-serif;
    font-weight: 400;
    font-size: 34px;
    letter-spacing: 2px;
    color: var(--brand-grey);
    margin: 0;
  }
</style>
</head>
<body>
<main class="canvas">

  <section class="postcard postcard--front" aria-label="Postcard front">
    <svg width="772" height="551" viewBox="0 0 772 551">
      <defs>
        <linearGradient id="sky-burst" x1="0" y1="0" x2="1" y2="0">
          <stop offset="0" stop-color="#b8201a"/>
          <stop offset="0.25" stop-color="#e2461e"/>
          <stop offset="0.45" stop-color="#f4a83a"/>
          <stop offset="0.62" stop-color="#e0502a"/>
          <stop offset="0.8" stop-color="#a8303a"/>
          <stop offset="1" stop-color="#3f6e70"/>
        </linearGradient>
        <linearGradient id="night-band" x1="0" y1="0" x2="0" y2="1">
          <stop offset="0" stop-color="#2a3f72"/>
          <stop offset="1" stop-color="#1a2a58"/>
        </linearGradient>
        <linearGradient id="ribbon-red" x1="0" y1="0" x2="0" y2="1">
          <stop offset="0" stop-color="#d82a26"/>
          <stop offset="1" stop-color="#a8141a"/>
        </linearGradient>
      </defs>

      <rect class="sky-burst" x="0" y="0" width="772" height="345" fill="url(#sky-burst)"
            role="img" aria-label="Sunburst rays in red, gold and teal with fireworks bursting"/>
      <rect class="night-band" x="0" y="342" width="772" height="209" fill="url(#night-band)"
            role="img" aria-label="Navy night sky with faint stars and fireworks"/>

      <g class="headline-block" text-anchor="middle" fill="var(--white)" stroke="var(--ink)" stroke-width="6" paint-order="stroke" stroke-linejoin="round">
        <text x="390" y="98" font-size="84" textLength="340" lengthAdjust="spacingAndGlyphs">WISHING</text>
        <text x="388" y="252" font-size="150" textLength="228" lengthAdjust="spacingAndGlyphs">YOU</text>
      </g>

      <g class="ribbon">
        <polygon points="176,270 240,258 220,300 246,338 176,338 196,304" fill="var(--red-deep)"/>
        <polygon points="632,270 568,258 588,300 562,338 632,338 612,304" fill="var(--red-deep)"/>
        <path d="M222,212 Q390,190 558,212 L566,286 Q390,262 214,286 Z" fill="url(#ribbon-red)"/>
        <text class="script" x="390" y="262" text-anchor="middle" font-size="50" fill="var(--white)">A Happy</text>
      </g>

      <rect class="flags" x="380" y="290" width="156" height="100" rx="4" fill="#c9cfe0" opacity="0.85"
            role="img" aria-label="Two small crossed American flags"/>

      <g class="date-block" fill="var(--white)" stroke="var(--ink)" stroke-width="4" paint-order="stroke">
        <text x="174" y="518" font-size="250" textLength="100" lengthAdjust="spacingAndGlyphs">4</text>
        <text x="286" y="372" font-size="84" textLength="80" lengthAdjust="spacingAndGlyphs">TH</text>
        <text x="274" y="518" font-size="190" textLength="266" lengthAdjust="spacingAndGlyphs">JULY</text>
      </g>
    </svg>
  </section>

  <section class="postcard postcard--back" aria-label="Postcard back">
    <svg width="428" height="551" viewBox="0 0 428 551" style="position:absolute;left:0;top:0">
      <defs>
        <linearGradient id="back-burst" x1="0" y1="0" x2="1" y2="1">
          <stop offset="0" stop-color="#c42418"/>
          <stop offset="0.4" stop-color="#f0a038"/>
          <stop offset="0.75" stop-color="#d84a22"/>
          <stop offset="1" stop-color="#8a1c1c"/>
        </linearGradient>
        <linearGradient id="back-night" x1="0" y1="0" x2="0" y2="1">
          <stop offset="0" stop-color="#4a1a18"/>
          <stop offset="1" stop-color="var(--night)"/>
        </linearGradient>
        <linearGradient id="back-ribbon" x1="0" y1="0" x2="0" y2="1">
          <stop offset="0" stop-color="#d82a26"/>
          <stop offset="1" stop-color="#a8141a"/>
        </linearGradient>
      </defs>

      <rect x="0" y="0" width="428" height="340" fill="url(#back-burst)"
            role="img" aria-label="Sunburst rays in red and gold with fireworks"/>
      <path d="M0,340 Q214,318 428,340 L428,551 L0,551 Z" fill="url(#back-night)"
            role="img" aria-label="Dark night sky with fireworks"/>

      <g class="burst-lines" stroke="var(--white)" stroke-width="4" stroke-linecap="round">
        <line x1="332" y1="44" x2="338" y2="14"/>
        <line x1="350" y1="54" x2="368" y2="30"/>
        <line x1="362" y1="72" x2="390" y2="60"/>
      </g>

      <g class="thanks-script" fill="var(--white)" stroke="var(--night)" stroke-width="3" paint-order="stroke" text-anchor="middle">
        <text x="210" y="150" font-size="118" textLength="340" lengthAdjust="spacingAndGlyphs">Thank</text>
        <text x="218" y="266" font-size="118" textLength="236" lengthAdjust="spacingAndGlyphs">You</text>
      </g>
      <text class="script" x="220" y="318" text-anchor="middle" font-size="32" fill="var(--white)" textLength="350" lengthAdjust="spacingAndGlyphs">For Being A Valued Client</text>

      <g class="date-block" fill="var(--white)" text-anchor="middle" transform="rotate(4 214 380)">
        <text x="214" y="384" font-size="44" textLength="290" lengthAdjust="spacingAndGlyphs">STAY SAFE AND</text>
        <text x="214" y="424" font-size="44" textLength="214" lengthAdjust="spacingAndGlyphs">ENJOY YOUR</text>
      </g>

      <g class="ribbon">
        <polygon points="18,452 80,440 64,478 86,512 18,510 36,478" fill="var(--red-deep)"/>
        <polygon points="398,470 336,448 350,488 326,520 396,528 378,496" fill="var(--red-deep)"/>
        <path d="M66,414 Q220,420 362,444 L350,508 Q210,482 56,478 Z" fill="url(#back-ribbon)"/>
        <g class="script" fill="var(--white)" text-anchor="middle" transform="rotate(4 210 460)">
          <text x="208" y="452" font-size="30">Independence Day</text>
          <text x="208" y="480" font-size="28">Celebrations!</text>
        </g>
      </g>
    </svg>

    <div class="address-side">
      <div class="stamp-box"></div>
      <div class="address-line" style="top:212px"></div>
      <div class="address-line" style="top:242px"></div>
      <div class="address-line" style="top:272px"></div>
      <div class="address-line" style="top:302px"></div>
      <p class="brand-name">HARTWELL LAW</p>
    </div>
  </section>

</main>
</body>
</html>
```